Centre Laser Vireloux

I need a trifold flyer for my new hair removal laser center. I saw your project for Plume center in canada and i like it. i want the same, or near the same. I'm french and i send you the text and the prices that I translated from the plume trifold. I have a logo . I like the grey and the pastel from plume flyer. Not sure that the pastel colour will agree with the red of my logo. But I don't think that you can replace the pastel with the red, so you will have to find another colour that fits well. ( gold ?) You will use some of my fotos of my website because we must show that it is for all skin colours

```html
<!DOCTYPE html>
<html lang="fr">
<head>
<meta charset="utf-8">
<title>Centre Laser Vireloux – Dépliant</title>
<link rel="stylesheet" href="https://fonts.googleapis.com/css2?family=Questrial&family=Mulish:wght@400;700;800&display=swap">
<style>
  :root {
    --page: #e6e6e6;
    --paper: #ffffff;
    --paper-shade: #bdbdbd;
    --ink: #3a3a3c;
    --ink-soft: #6b6b6e;
    --dark: #3f3f42;
    --gold: #c49b6c;
    --photo-light: #b9b4ae;
    --photo-dark: #4a4644;
  }
  * { box-sizing: border-box; margin: 0; padding: 0; }
  html, body { width: 1200px; height: 800px; overflow: hidden; background: var(--page); }
  body { font-family: "Mulish", sans-serif; color: var(--ink); }

  .trifold {
    position: absolute; left: 45px; top: 30px;
    width: 1110px; height: 740px;
    display: flex;
    box-shadow: 0 10px 30px rgba(0,0,0,.12);
  }
  .panel { position: relative; width: 370px; height: 740px; overflow: hidden; }
  .panel > svg.shapes { position: absolute; inset: 0; width: 100%; height: 100%; }

  /* brand name, set as plain text */
  .brand { position: relative; text-align: center; font-family: "Questrial", sans-serif; font-weight: 400; color: var(--ink-soft); line-height: 1; }
  .brand__name { display: block; font-size: 26px; letter-spacing: .5px; }
  .brand__place { display: block; font-size: 11px; letter-spacing: 2px; margin-top: 4px; text-transform: uppercase; }
  .brand--large .brand__name { font-size: 36px; }
  .brand--large .brand__place { font-size: 14px; letter-spacing: 2.5px; }
  .brand--light { color: #e4e4e4; }

  /* left panel */
  .panel--info { background: linear-gradient(110deg, var(--paper-shade) 0%, #e8e8e8 45%, var(--paper) 100%); }
  .panel--info .content { position: relative; padding: 90px 44px 0 40px; }
  .panel--info .brand { margin-bottom: 42px; }
  .copy { font-size: 11.5px; line-height: 1.45; margin-bottom: 30px; }
  .copy h3 { font-size: 12.5px; font-weight: 800; margin-bottom: 8px; }

  /* middle panel */
  .panel--contact { background: linear-gradient(100deg, #cfcfcf 0%, #f4f4f4 30%, var(--paper) 60%); }
  .panel--contact .content { position: relative; padding: 240px 34px 0 34px; }
  .panel--contact .brand { margin-bottom: 34px; }
  .intro { font-size: 12.5px; font-weight: 700; line-height: 1.45; }
  .contacts { position: absolute; left: 34px; top: 520px; list-style: none; font-size: 8.5px; font-weight: 700; }
  .contacts li { display: flex; align-items: center; gap: 12px; margin-bottom: 16px; }
  .contacts svg { width: 20px; height: 20px; flex: none; }
  .social { position: absolute; left: 140px; top: 640px; display: flex; gap: 10px; }
  .social span { width: 18px; height: 18px; border-radius: 50%; background: var(--ink); }

  /* right panel */
  .panel--cover { background: var(--dark); color: #e4e4e4; }
  .panel--cover .content { position: relative; padding: 68px 30px 0; text-align: center; }
  .tagline { font-size: 11.5px; line-height: 1.5; margin-top: 30px; color: #dcdcdc; }
  .website { position: absolute; right: 34px; bottom: 36px; font-size: 10px; letter-spacing: .5px; color: #dcdcdc; }
</style>
</head>
<body>
<main class="trifold">

  <section class="panel panel--info">
    <div class="content">
      <div class="brand">
        <span class="brand__name">Centre Laser</span>
        <span class="brand__place">Vireloux</span>
      </div>
      <p class="copy">Lorem ipsum dolor sit amet, consectetur adipiscing elit, sed do eiusmod tempor incididunt ut labore et dolore magna aliqua. Ut enim ad minim veniam, quis nostrud exercitation ullamco laboris nisi ut aliquip ex ea commodo consequat.</p>
      <div class="copy">
        <h3>Lorem ipsum dolor</h3>
        <p>Duis aute irure dolor in reprehenderit in voluptate velit esse cillum dolore eu fugiat nulla pariatur. Excepteur sint occaecat cupidatat non proident, sunt in culpa qui officia deserunt mollit anim id est laborum.</p>
      </div>
      <div class="copy">
        <h3>Lorem ipsum dolor</h3>
        <p>Lorem ipsum dolor sit amet, consectetur adipiscing elit, sed do eiusmod tempor incididunt ut labore et dolore magna aliqua. Ut enim ad minim veniam, quis nostrud exercitation ullamco laboris nisi ut aliquip ex ea commodo consequat. Duis aute irure dolor in reprehenderit in voluptate velit esse cillum dolore eu fugiat nulla pariatur. Excepteur sint occaecat cupidatat non proident, sunt in culpa qui officia deserunt mollit anim id est laborum.</p>
      </div>
      <div class="copy">
        <h3>Lorem ipsum dolor</h3>
        <p>Duis aute irure dolor in reprehenderit in voluptate velit esse cillum dolore eu fugiat nulla pariatur. Excepteur sint occaecat cupidatat non proident, sunt in culpa qui officia deserunt mollit anim id est laborum.</p>
      </div>
    </div>
  </section>

  <section class="panel panel--contact">
    <svg class="shapes" viewBox="0 0 370 740" preserveAspectRatio="none">
      <defs>
        <linearGradient id="portraitTone" x1="0" y1="0" x2="1" y2="1">
          <stop offset="0" stop-color="var(--photo-light)"/>
          <stop offset="1" stop-color="var(--photo-dark)"/>
        </linearGradient>
      </defs>
      <path role="img" aria-label="Photo en noir et blanc d'un homme torse nu" d="M0,0 H370 V150 C220,178 80,120 0,0 Z" fill="url(#portraitTone)"/>
      <path d="M0,0 C80,120 220,178 370,150" fill="none" stroke="var(--gold)" stroke-width="14"/>
      <path d="M150,740 C230,700 300,640 370,585 V740 Z" fill="var(--dark)"/>
      <path d="M150,740 C230,700 300,640 370,585" fill="none" stroke="var(--gold)" stroke-width="10"/>
    </svg>
    <div class="content">
      <div class="brand brand--large">
        <span class="brand__name">Centre Laser</span>
        <span class="brand__place">Vireloux</span>
      </div>
      <p class="intro">Lorem ipsum dolor sit amet, consectetur adipiscing elit, sed do eiusmod tempor incididunt ut labore et dolore magna aliqua. Ut enim ad minim veniam, quis nostrud exercitation ullamco laboris nisi ut aliquip ex ea commodo consequat.</p>
    </div>
    <ul class="contacts">
      <li>
        <svg viewBox="0 0 20 20"><path d="M10 1a6 6 0 0 0-6 6c0 5 6 12 6 12s6-7 6-12a6 6 0 0 0-6-6z" fill="var(--ink)"/><circle cx="10" cy="7" r="2.3" fill="#fff"/></svg>
        <span>Sed ut perspiciatis unde omnis iste natus error sit<br>voluptatem</span>
      </li>
      <li>
        <svg viewBox="0 0 20 20"><path d="M5 2l3 4-2 2c1 2.5 3.5 5 6 6l2-2 4 3-2 3C9 18 2 11 2 4z" fill="var(--ink)"/></svg>
        <span>123-456-7890</span>
      </li>
      <li>
        <svg viewBox="0 0 20 20"><circle cx="10" cy="10" r="8" fill="var(--ink)"/><g fill="none" stroke="#fff" stroke-width="1"><ellipse cx="10" cy="10" rx="3.5" ry="8"/><path d="M2 10h16M3.5 6h13M3.5 14h13"/></g></svg>
        <span>www.vireloux-laser.fr</span>
      </li>
    </ul>
    <div class="social" aria-label="Réseaux sociaux"><span></span><span></span><span></span></div>
  </section>

  <section class="panel panel--cover">
    <svg class="shapes" viewBox="0 0 370 740" preserveAspectRatio="none">
      <defs>
        <linearGradient id="coverTone" x1="0" y1="0" x2="1" y2="1">
          <stop offset="0" stop-color="#6e6a68"/>
          <stop offset=".55" stop-color="#b46a45"/>
          <stop offset="1" stop-color="#d9a789"/>
        </linearGradient>
      </defs>
      <path role="img" aria-label="Portrait d'une femme aux cheveux roux" d="M0,228 C140,215 260,235 322,300 C372,360 362,520 282,590 C212,650 80,645 0,615 Z" fill="url(#coverTone)"/>
      <path d="M0,228 C140,215 260,235 322,300 C372,360 362,520 282,590 C212,650 80,645 0,615" fill="none" stroke="var(--gold)" stroke-width="12"/>
    </svg>
    <div class="content">
      <div class="brand brand--light">
        <span class="brand__name">Centre Laser</span>
        <span class="brand__place">Vireloux</span>
      </div>
      <p class="tagline">Epilation toute peau même bronzée, toute l'année, au<br>Laser médical classe IV Lumentis Nd:YAG.<br>Tout genre.</p>
    </div>
    <p class="website">www.vireloux-laser.fr</p>
  </section>

</main>
</body>
</html>
```